Identity Package (Logo, Website)

We need a logo and website design for a new company.
The new company is a voicemail transcription service provider. It's name is KL9BQZ.io
It will be very transactional. We like the "bootstrap" look and feel, and will be using a developer familiar with bootstrap. Here are the kinds of webpages we like :
https://www.lumenvane.io
http://www.quorbil.com/
http://www.plenivo.com/
There will only be 5 pages, as follows :
1- Homepage
2- Voicemail Transcription for Individuals
3- Voicemail Transcription for Companies
4- Wholesale Voicemail Transcription for Service Providers/Enterprises
5- Contact us
As far as the logo is concerned, we'd like to have just stylized text. It should be done in such a way as to make it easy to see the different elements of the name, which are KL, 2, and BQZ.
Reason: I have received a number of designs, but the designs are mostly from the same few designers (not that much variety in designers). I'd like a few more to compare if possible, so I thought I would keep this open until Monday to give more designers the opportunity to submit over the weekend. Thanks!

```html
<!DOCTYPE html>
<html lang="en">
<head>
<meta charset="utf-8">
<title>KL9BQZ.io — Voicemail Transcription</title>
<link href="https://fonts.googleapis.com/css2?family=Open+Sans:wght@400;600;700&family=Arimo:wght@400;700&display=swap" rel="stylesheet">
<style>
:root{
  --blue:#2a9fd8;
  --blue-dark:#1d85bd;
  --blue-light:#5cc0ea;
  --red:#d9394a;
  --red-light:#e9616d;
  --ink:#222;
  --text:#444;
  --muted:#666;
  --footer:#2b2b2b;
  --white:#fff;
}
*{box-sizing:border-box;margin:0;padding:0}
html,body{width:735px;height:1200px;overflow:hidden;background:var(--white)}
body{position:relative;font-family:"Arimo",Arial,sans-serif;color:var(--text)}

/* header */
.site-header{position:absolute;left:0;top:0;width:735px;height:54px;background:var(--white);box-shadow:0 1px 3px rgba(0,0,0,.08);z-index:2}
.brand{position:absolute;left:105px;top:15px;font-family:"Open Sans",sans-serif;font-weight:700;font-size:18px;line-height:24px;color:var(--ink);letter-spacing:-.3px}
.nav a{position:absolute;top:0;height:54px;line-height:54px;font-family:"Open Sans",sans-serif;font-size:10px;color:var(--ink);text-decoration:none}
.nav .active{background:var(--blue);color:var(--white);width:42px;text-align:center}
.btn-signup{position:absolute;left:588px;top:22px;width:43px;height:14px;background:var(--red);color:var(--white);font-family:"Open Sans",sans-serif;font-size:7.5px;line-height:14px;text-align:center;border-radius:2px}

/* hero */
.hero{position:absolute;left:0;top:54px;width:735px;height:322px;background:linear-gradient(90deg,#d6d8da 0%,#e9e4dc 35%,#d8d2c4 65%,#cfc8b8 100%)}
.hero-photo{position:absolute;left:0;top:0;width:330px;height:322px;background:radial-gradient(ellipse at 50% 45%,#e8c6a8 0%,#d9b493 30%,#b9a489 55%,rgba(200,196,190,0) 80%)}
.hero-title{position:absolute;left:332px;top:178px;font-family:"Open Sans",sans-serif;color:var(--ink)}
.hero-title .l1{font-size:12.5px;display:block}
.hero-title .l2{font-size:15px;display:block;margin-top:6px}
.slider-ctrl{position:absolute;left:526px;top:288px;width:96px;height:15px;background:#f4f4f4;border:1px solid #bbb;border-radius:3px}

/* welcome */
.welcome{position:absolute;left:0;top:376px;width:735px;height:102px;background:linear-gradient(#fafafa,#e4e4e4);text-align:center}
.welcome h1{margin-top:12px;font-family:"Open Sans",sans-serif;font-weight:600;font-size:13.5px;color:var(--ink)}
.welcome p{width:472px;margin:5px auto 0;font-size:8.6px;line-height:14px;color:var(--muted)}
.btn-blue{display:block;background:linear-gradient(var(--blue-light),var(--blue-dark));color:var(--white);font-family:"Open Sans",sans-serif;font-weight:700;text-align:center;border-radius:2px}
.welcome .btn-blue{position:absolute;left:333px;top:72px;width:73px;height:19px;line-height:19px;font-size:7.5px}

/* services */
.service{position:absolute;top:495px;width:150px;text-align:center}
.service h2{margin-top:8px;font-family:"Open Sans",sans-serif;font-weight:400;font-size:8.3px;line-height:10.5px;color:#333}
.btn-red-sm{display:inline-block;margin-top:8px;width:54px;height:15px;line-height:15px;background:linear-gradient(var(--red-light),var(--red));color:var(--white);font-size:6px;border-radius:2px}
.divider{position:absolute;left:0;top:644px;width:735px;height:1px;background:#cfcfcf}

/* benefits */
.benefits-band{position:absolute;left:0;top:645px;width:735px;height:193px;background:linear-gradient(#f7f7f7,#e2e2e2);border-bottom:1px solid #d0d0d0}
.video{position:absolute;left:108px;top:17px;width:282px;height:160px}
.benefits{position:absolute;left:418px;top:18px;width:213px}
.benefits h3{font-family:"Open Sans",sans-serif;font-weight:400;font-size:11.5px;color:var(--ink);padding-bottom:3px;border-bottom:1px solid var(--blue)}
.benefits ul{list-style:none;margin-top:6px}
.benefits li{font-family:"Open Sans",sans-serif;font-size:7px;height:18px;color:#222;display:flex;align-items:center;gap:6px}
.benefits li::before{content:"";width:4px;height:4px;background:var(--blue-dark);flex:none}

/* pricing */
.pricing-title{position:absolute;left:0;top:858px;width:735px;text-align:center;font-family:"Open Sans",sans-serif;font-weight:400;font-size:11.5px;color:var(--ink)}
.plan{position:absolute;top:894px;width:165px;height:210px;background:linear-gradient(#fff 30%,#dcdcdc);box-shadow:0 8px 8px -6px rgba(0,0,0,.35);text-align:center}
.plan-head{height:51px;padding-top:11px;font-family:"Open Sans",sans-serif;font-weight:700;font-size:10.5px;color:var(--white)}
.plan-blue .plan-head{background:linear-gradient(var(--blue-light),#48b0e0)}
.plan-red .plan-head{background:linear-gradient(#ee6f7b,var(--red))}
.price{position:absolute;left:58px;top:28px;width:48px;height:48px;border-radius:50%;color:var(--white);font-family:"Open Sans",sans-serif;font-size:19px;line-height:48px;letter-spacing:-1px}
.plan-blue .price{background:var(--blue-dark)}
.plan-red .price{background:var(--red)}
.plan ul{list-style:none;margin-top:40px;font-size:8.5px;color:#555}
.plan li{height:22.5px}
.plan li b{color:#333}
.plan .btn{position:absolute;left:39px;top:166px;width:90px;height:27px;line-height:27px;font-family:"Open Sans",sans-serif;font-weight:700;font-size:8.5px;color:var(--white);border-radius:2px}
.plan-blue .btn{background:linear-gradient(var(--blue-light),var(--blue-dark))}
.plan-red .btn{background:linear-gradient(var(--red-light),var(--red))}

/* footer */
.site-footer{position:absolute;left:0;top:1130px;width:735px;height:70px;background:var(--footer)}
.site-footer .brand{left:105px;top:23px;color:#e8e8e8;font-size:14.5px}
.copyright{position:absolute;left:300px;top:31px;width:200px;text-align:center;font-size:6.5px;color:#ddd}
.social{position:absolute;left:549px;top:25px;display:flex;gap:3px}
.social span{width:13px;height:13px;border-radius:2px}
</style>
</head>
<body>

<header class="site-header">
  <div class="brand">KL9BQZ.IO</div>
  <nav class="nav">
    <a class="active" style="left:296px">HOME</a>
    <a style="left:347px">FEATURES</a>
    <a style="left:406px">PRICING</a>
    <a style="left:457px">CUSTOMERS</a>
    <a style="left:528px">LOG IN</a>
  </nav>
  <span class="btn-signup">SIGN UP</span>
</header>

<section class="hero">
  <div class="hero-photo" role="img" aria-label="Photo of a smiling support agent wearing a headset in a bright office"></div>
  <div class="hero-title">
    <span class="l1">EVERYTHING YOU NEED TO BUILD AN ENTERPRISE</span>
    <span class="l2">VOICEMAIL TRANSCRIPTION&nbsp; APPLICATION</span>
  </div>
  <div class="slider-ctrl">
    <svg width="96" height="15" viewBox="0 0 96 15">
      <path d="M10 4 L7 7.5 L10 11" stroke="#333" stroke-width="1.4" fill="none"/>
      <path d="M18 4 L21 7.5 L18 11" stroke="#555" stroke-width="1.2" fill="none"/>
      <line x1="27" y1="2" x2="27" y2="13" stroke="#ccc"/>
      <circle cx="36" cy="7.5" r="2" fill="#aaa"/>
      <circle cx="46" cy="7.5" r="2" fill="#aaa"/>
      <circle cx="56" cy="7.5" r="2" fill="#333"/>
      <circle cx="66" cy="7.5" r="2" fill="#aaa"/>
      <circle cx="76" cy="7.5" r="2" fill="#aaa"/>
      <circle cx="86" cy="7.5" r="2" fill="#aaa"/>
    </svg>
  </div>
</section>

<section class="welcome">
  <h1>WELCOM TO VOICEMAIL TRANSCRIPTION</h1>
  <p>We believe in creating lasting value for brands rather than disposable digital marketing. That means we focus on building products, experiences and platforms that have the power to transform a brand and the web</p>
  <span class="btn-blue">READ MORE</span>
</section>

<section class="services">
  <div class="service" style="left:116px">
    <svg width="74" height="74" viewBox="0 0 74 74"><circle cx="37" cy="37" r="35" fill="#fff" stroke="#2a9fd8" stroke-width="2"/><circle cx="37" cy="30" r="12" fill="#2a9fd8"/><path d="M18 56 Q37 36 56 56 Z" fill="#2a9fd8"/></svg>
    <h2>VOICEMAIL TRANSCRIPTION<br>FOR INDIVIDUALS</h2>
    <span class="btn-red-sm">READ MORE</span>
  </div>
  <div class="service" style="left:294px">
    <svg width="74" height="74" viewBox="0 0 74 74"><circle cx="37" cy="37" r="35" fill="#fff" stroke="#2a9fd8" stroke-width="2"/><circle cx="37" cy="37" r="21" fill="#2a9fd8"/><ellipse cx="37" cy="37" rx="9" ry="21" fill="none" stroke="#fff" stroke-width="2"/><line x1="16" y1="37" x2="58" y2="37" stroke="#fff" stroke-width="2"/></svg>
    <h2>VOICEMAIL TRANSCRIPTION<br>FOR COMPANIES</h2>
    <span class="btn-red-sm">READ MORE</span>
  </div>
  <div class="service" style="left:473px">
    <svg width="74" height="74" viewBox="0 0 74 74"><circle cx="37" cy="37" r="35" fill="#fff" stroke="#2a9fd8" stroke-width="2"/><circle cx="30" cy="30" r="9" fill="#2a9fd8"/><circle cx="45" cy="30" r="9" fill="#2a9fd8" stroke="#fff" stroke-width="2"/><path d="M14 54 Q30 36 46 54 Z" fill="#2a9fd8"/><path d="M30 54 Q45 36 60 54 Z" fill="#2a9fd8" stroke="#fff" stroke-width="2"/></svg>
    <h2>WHOLESALE VOICEMAIL<br>TRANSCRIPTION FOR ENTERPRISES</h2>
    <span class="btn-red-sm">READ MORE</span>
  </div>
</section>
<div class="divider"></div>

<section class="benefits-band">
  <svg class="video" viewBox="0 0 282 160" role="img" aria-label="Laptop showing the product introduction video">
    <defs><linearGradient id="screen" x1="0" y1="0" x2="1" y2="1"><stop offset="0" stop-color="#f2f2f2"/><stop offset="1" stop-color="#cfcfcf"/></linearGradient></defs>
    <rect x="27" y="0" width="228" height="154" rx="6" fill="#2b2b2b"/>
    <rect x="34" y="9" width="214" height="140" fill="url(#screen)"/>
    <rect x="0" y="153" width="282" height="7" rx="3" fill="#d6d6d6"/>
    <circle cx="139" cy="72" r="25" fill="#555" opacity=".8"/>
    <path d="M132 60 L151 72 L132 84 Z" fill="#fff"/>
  </svg>
  <div class="benefits">
    <h3>BENEFITS</h3>
    <ul>
      <li>EASY TO USE &amp; COMPLETELY SELF-DIRECTED</li>
      <li>REDUCE TIME AND COST SPENT INTERVIEWING</li>
      <li>INTERVIEW CANDIDATES FROM ANYWHERE IN THE WORLD</li>
      <li>NO NEED TO EVALUATE CANDIDATES FROM MEMORY</li>
      <li>IMPROVE TALENT ACQUISITION</li>
      <li>INVITE ANYONE TO REVIEW CANDIDATES</li>
      <li>CUSTOM SECURITY</li>
    </ul>
  </div>
</section>

<h2 class="pricing-title">PRICING THAT SCALES WITH YOU AS YOU GROW</h2>

<div class="plan plan-blue" style="left:105px">
  <div class="plan-head">WEEKLY PACKAGES</div>
  <div class="price">$50</div>
  <ul><li><b>10</b> Users</li><li><b>10 GB</b> amount of space</li><li><b>5</b> Email account</li></ul>
  <span class="btn">CLICK HERE</span>
</div>
<div class="plan plan-red" style="left:286px">
  <div class="plan-head">MONTHLY PACKAGES</div>
  <div class="price">$250</div>
  <ul><li><b>10</b> Users</li><li><b>10 GB</b> amount of space</li><li><b>5</b> Email account</li></ul>
  <span class="btn">CLICK HERE</span>
</div>
<div class="plan plan-blue" style="left:465px">
  <div class="plan-head">YEARLY PACKAGES</div>
  <div class="price">$950</div>
  <ul><li><b>10</b> Users</li><li><b>10 GB</b> amount of space</li><li><b>5</b> Email account</li></ul>
  <span class="btn">CLICK HERE</span>
</div>

<footer class="site-footer">
  <div class="brand">KL9BQZ.IO</div>
  <p class="copyright">Copyright © 2014. All rights reserved.</p>
  <div class="social" aria-label="Social links">
    <span style="background:#d9473a"></span>
    <span style="background:#3b5a99"></span>
    <span style="background:#2aa3dc"></span>
    <span style="background:#c8232c"></span>
    <span style="background:#f08a24"></span>
  </div>
</footer>

</body>
</html>
```